Event Manager Business Card Design

I am a freelance event manager and work on high end events such as film premieres, product launches and black tie charity dinners. I would like the design to reflect efficiency, reliability, creativity and passion. I am a French Canadian who is now living and working in Sydney, Australia and although I will not be doing any business in Canada, perhaps a Canadian element can be incorporated in the business card to make my card stand out? I would like there to be some white space on the card to allow people to write on it, but not too much. I also want both sides of the card to be used. As a freelancer, I will be handing out my card to anyone with an outstretched hand. It's safe to assume that anyone who gets my card will be receiving hundreds of business cards at a time, so I really need mine to stand out. Please be original! I kind of want people reaction when they receive my card to be "wow, this guy means business, cool card".

Industry/Entity Type

Charity

Contact Information for Business Card

Marc Velline
Event Manager
+61 437 602 915
mvelline4@quorvix.com
brentlo.com/in/marcvelline

Requirements
Should not have
• Cliché event management elements (no film reels, no top hats, etc.)

```html
<!DOCTYPE html>
<html lang="en">
<head>
<meta charset="utf-8">
<title>Marc Velline – Event Manager Business Card</title>
<link rel="stylesheet" href="https://fonts.googleapis.com/css2?family=Jost:wght@400;500;600&display=swap">
<style>
  :root {
    --backdrop: #e4e2df;
    --card-white: #f1f2f2;
    --brand-green: #1f9e45;
    --ink: #4a4a4c;
    --card-shadow: rgba(0, 0, 0, 0.18);
  }
  * { box-sizing: border-box; margin: 0; padding: 0; }
  html, body {
    width: 1200px;
    height: 880px;
    overflow: hidden;
  }
  body {
    background: var(--backdrop);
    font-family: "Jost", "Futura", sans-serif;
    color: var(--ink);
  }
  .card-sheet {
    width: 1200px;
    height: 880px;
    display: flex;
    align-items: center;
    justify-content: center;
    gap: 40px;
  }
  .card {
    position: relative;
    width: 560px;
    height: 320px;
    background: var(--card-white);
    box-shadow: 0 6px 18px var(--card-shadow);
    overflow: hidden;
  }
  .card-art {
    position: absolute;
    inset: 0;
    width: 100%;
    height: 100%;
  }
  .card-art .green { fill: var(--brand-green); }

  /* front */
  .identity {
    position: absolute;
    left: 0;
    right: 62px;
    top: 148px;
    text-align: right;
  }
  .identity-name {
    font-size: 36px;
    font-weight: 600;
    letter-spacing: 0.2px;
    line-height: 1;
  }
  .identity-role {
    margin-top: 4px;
    margin-right: 34px;
    font-size: 18px;
    font-weight: 400;
  }
  .contact-line {
    position: absolute;
    left: 24px;
    right: 20px;
    bottom: 42px;
    display: flex;
    align-items: baseline;
    gap: 12px;
    font-size: 16.5px;
    white-space: nowrap;
  }
  .contact-label {
    color: var(--brand-green);
    font-weight: 600;
  }
  .contact-divider { margin: 0 4px; }

  /* back */
  .web-address {
    position: absolute;
    left: 330px;
    top: 14px;
    width: 24px;
    height: 230px;
    display: flex;
    align-items: center;
    justify-content: center;
  }
  .web-address span {
    display: block;
    transform: rotate(90deg);
    white-space: nowrap;
    color: var(--card-white);
    font-size: 22px;
    font-weight: 500;
    letter-spacing: 0.5px;
  }
</style>
</head>
<body>
<main class="card-sheet">

  <section class="card card-front" aria-label="Card front">
    <svg class="card-art" viewBox="0 0 560 320" aria-hidden="true">
      <polygon class="green" points="356,0 412,0 412,62 446,62 384,140 322,62 356,62"/>
    </svg>
    <div class="identity">
      <h1 class="identity-name">Marc Velline</h1>
      <p class="identity-role">Event Manager</p>
    </div>
    <p class="contact-line">
      <span><span class="contact-label">cell:</span> +61 437 602 915</span>
      <span class="contact-divider">|</span>
      <span><span class="contact-label">e-mail:</span> mvelline4@quorvix.com</span>
    </p>
  </section>

  <section class="card card-back" aria-label="Card back">
    <svg class="card-art" viewBox="0 0 560 320" aria-hidden="true">
      <polygon class="green" points="0,0 364,0 364,256 300,320 0,320"/>
      <polygon class="green" points="456,98 560,98 560,252 456,252"/>
    </svg>
    <p class="web-address"><span>www.velline.com</span></p>
  </section>

</main>
</body>
</html>
```